Buchcover für mittelständige Unternehmen die positive Bewertungen erhalten möchten
Zielgruppe
Was macht die Firma: Unternehmensberatung für den Personlabereich
Zielgruppe: Unternehmer aus dem mittelständigen Bereich die positive Bewertungen auf Portalen wie werkrat, deskmirror und Plomix erhalten möchten.
Aufgabenstellung
Ansprechend, Professionell, Positive Aussendarstellung des Unternehmens

```html
<!DOCTYPE html>
<html lang="de">
<head>
<meta charset="utf-8">
<title>Wir bringen Sie zum Erfolg – Buchcover</title>
<link rel="stylesheet" href="https://fonts.googleapis.com/css2?family=Poppins:wght@700&family=Didact+Gothic&display=swap">
<style>
  :root {
    --backdrop: #dfe6ea;
    --cover-white: #ffffff;
    --title-teal: #0f4560;
    --author-ink: #2a2a2a;
    --band-blue: #bcd6e2;
    --photo-light: #cfd5da;
    --photo-mid: #6f7880;
    --photo-dark: #2b3036;
    --fold-shade: #ececec;
  }
  html, body {
    margin: 0;
    padding: 0;
    width: 1200px;
    height: 848px;
    overflow: hidden;
    background: var(--backdrop);
  }
  .canvas {
    position: relative;
    width: 1200px;
    height: 848px;
  }
  .book-cover {
    position: absolute;
    left: 320px;
    top: 34px;
    width: 560px;
    height: 780px;
    background: var(--cover-white);
    box-shadow: 0 10px 30px rgba(40, 60, 75, 0.18);
    overflow: hidden;
  }
  .cover-art {
    position: absolute;
    inset: 0;
    width: 560px;
    height: 780px;
  }
  .cover-title {
    position: absolute;
    left: 40px;
    top: 372px;
    margin: 0;
    font-family: "Poppins", sans-serif;
    font-weight: 700;
    font-size: 42px;
    line-height: 1.08;
    letter-spacing: -0.5px;
    color: var(--title-teal);
  }
  .cover-subtitle {
    position: absolute;
    left: 40px;
    top: 470px;
    margin: 0;
    font-family: "Didact Gothic", sans-serif;
    font-size: 15px;
    color: var(--title-teal);
  }
  .cover-author {
    position: absolute;
    left: 0;
    right: 0;
    bottom: 44px;
    margin: 0;
    text-align: center;
    font-family: "Didact Gothic", sans-serif;
    font-size: 21px;
    color: var(--author-ink);
  }
</style>
</head>
<body>
<main class="canvas">
  <article class="book-cover">
    <svg class="cover-art" viewBox="0 0 560 780" xmlns="http://www.w3.org/2000/svg">
      <defs>
        <linearGradient id="photoTone" x1="0" y1="0" x2="1" y2="1">
          <stop offset="0" stop-color="var(--photo-light)"/>
          <stop offset="0.45" stop-color="var(--photo-mid)"/>
          <stop offset="1" stop-color="var(--photo-dark)"/>
        </linearGradient>
        <linearGradient id="bandTone" x1="0" y1="0" x2="1" y2="1">
          <stop offset="0" stop-color="var(--band-blue)"/>
          <stop offset="1" stop-color="#4d6272"/>
        </linearGradient>
      </defs>
      <rect class="cover-photo" x="0" y="0" width="560" height="640" fill="url(#photoTone)"
            role="img" aria-label="Foto: Geschäftsmann im Anzug tippt auf eine Reihe leuchtender Bewertungssterne"/>
      <polygon class="accent-band" points="0,215 440,640 430,640 0,330" fill="url(#bandTone)" opacity="0.85"/>
      <polygon class="white-panel" points="0,330 430,640 560,560 560,780 0,780" fill="var(--cover-white)"/>
      <polygon class="fold-shade" points="260,780 560,600 560,620 320,780" fill="var(--fold-shade)"/>
    </svg>
    <h1 class="cover-title">Wir bringen<br>Sie zum Erfolg</h1>
    <p class="cover-subtitle">Das Geheimnis hinter Top Bewertungen</p>
    <p class="cover-author">Max Mustermann</p>
  </article>
</main>
</body>
</html>
```